Business Cards- The Manor at Brookridge Golf Club

We would like our business cards to look more high-end. We are a wedding venue that has been in business for 60+ years. We like our logo and our colors - primarily green and a touch of gold/beige. The owner wants our business cards to look more special..

Target Market(s)

Brides who have already toured our venue

Industry/Entity Type

Wedding venue - mansion

Contact Information for Business Card

Name, email, physical address, phone number

Colors
00AB8E
00BBA5
67D7C9
C6EFE9
E9F9F6

Requirements
Must have
• I think we would like our cards to be so pretty that people will want to keep them and will remember the venue. The venue is historic (built in 1850) and beautiful.
Nice to have
• Could we put an image of the building on one side and the contact info on the other?
Should not have
• The color black

```html
<!DOCTYPE html>
<html lang="en">
<head>
<meta charset="utf-8">
<title>The Manor at Brookridge Golf Club – Business Cards</title>
<link rel="stylesheet" href="https://fonts.googleapis.com/css2?family=Montserrat:wght@400;500&display=swap">
<style>
  :root {
    --page-bg: #e6e8e4;
    --card-green: #8ca43f;
    --brand-green: #7a9a2e;
    --back-ink: #e3ebc6;
    --gold: #d9cba3;
    --paper: #ffffff;
    --ink: #4a4f45;
    --shadow: rgba(40, 50, 30, 0.18);
  }
  * { box-sizing: border-box; margin: 0; padding: 0; }
  html, body {
    width: 1200px;
    height: 1186px;
    overflow: hidden;
    background: var(--page-bg);
    font-family: "Montserrat", sans-serif;
  }
  .sheet { position: relative; width: 1200px; height: 1186px; }
  .card {
    position: absolute;
    left: 160px;
    width: 880px;
    height: 503px;
    border-radius: 34px;
    overflow: hidden;
    box-shadow: 0 18px 40px var(--shadow);
  }
  .card--back {
    top: 60px;
    background: var(--card-green);
    display: flex;
    align-items: center;
    justify-content: center;
  }
  .card--front { top: 623px; background: var(--paper); }

  /* Wordmark */
  .wordmark { display: flex; align-items: center; }
  .wordmark__name { font-weight: 500; line-height: 1.15; }
  .wordmark__dot { flex: none; border-radius: 50%; background: var(--gold); }

  .card--back .wordmark { gap: 30px; }
  .card--back .wordmark__name {
    font-size: 58px;
    color: var(--back-ink);
    letter-spacing: 1px;
  }
  .card--back .wordmark__dot { width: 78px; height: 78px; }

  .card--front .wordmark {
    position: absolute;
    left: 56px;
    top: 62px;
    gap: 14px;
  }
  .card--front .wordmark__name {
    font-size: 22px;
    color: var(--brand-green);
    letter-spacing: 0.3px;
  }
  .card--front .wordmark__dot { width: 36px; height: 36px; }

  /* Building photo area */
  .card__photo { position: absolute; inset: 0; width: 880px; height: 503px; }

  /* Contact block */
  .contact { position: absolute; left: 56px; bottom: 50px; color: var(--ink); }
  .contact__name {
    font-size: 31px;
    font-weight: 500;
    color: var(--brand-green);
    letter-spacing: 0.5px;
  }
  .contact__title { font-size: 17px; margin-top: 6px; }
  .contact__rule {
    width: 24px;
    height: 2px;
    background: var(--brand-green);
    margin: 18px 0 16px;
  }
  .contact__list { list-style: none; font-size: 17px; line-height: 1.6; }
</style>
</head>
<body>
<main class="sheet">

  <section class="card card--back">
    <div class="wordmark">
      <span class="wordmark__name">The Manor at<br>Brookridge Golf Club</span>
      <span class="wordmark__dot"></span>
    </div>
  </section>

  <section class="card card--front">
    <svg class="card__photo" viewBox="0 0 880 503" role="img" aria-label="Photograph of the white historic manor house with its curved columned porch, dormer windows and trimmed hedges at dusk">
      <defs>
        <linearGradient id="building-tones" x1="0" y1="0" x2="0" y2="1">
          <stop offset="0" stop-color="#aebccb"/>
          <stop offset="0.45" stop-color="#dde2e6"/>
          <stop offset="0.75" stop-color="#9aa39a"/>
          <stop offset="1" stop-color="#3f5a35"/>
        </linearGradient>
      </defs>
      <path d="M385,0 C372,230 510,440 705,503 L880,503 L880,0 Z" fill="url(#building-tones)"/>
    </svg>

    <div class="wordmark">
      <span class="wordmark__dot"></span>
      <span class="wordmark__name">The Manor at<br>Brookridge Golf Club</span>
    </div>

    <div class="contact">
      <h1 class="contact__name">Helen Marlowe</h1>
      <p class="contact__title">President - owner</p>
      <div class="contact__rule"></div>
      <ul class="contact__list">
        <li>C : (555) 014-3829</li>
        <li>M : hmarlowe@brookridgegolfclub.com</li>
        <li>A : 48 Larkspur Lane. Fairhaven, MD 21000</li>
      </ul>
    </div>
  </section>

</main>
</body>
</html>
```